out of the box Business Card Design for a Manufacturer / Distributor

We are a manufarturer and distributor of products.
the company name is Vortani (Pic attached)

the picture is NOT a must have on the business Card.

the Business Card should look really professional and/or special, so out of the box thinking is welcome.

there should be 2 Adresses on the Business Card for Main and Branch Office.
Email Adress, homepage, Name is required
NO Phone Number

Our working field:
Private Labeling
high Quality Production
direct distribution
warehousing
trademark registration
legal support

Main Office:
Kornblumenweg 14
08352 Burgstädt
Germany

Branch Office:
Daska Lane
Sialkot
Pakistan

Names:
Lukas Feldhaus (Owner)
Imran Qureshi (Owner)

Email:
lukas@vortani-example.com
imran@vortani-example.com

homepage:
vortani-example.com

Industry/Entity Type

Manufacturer Distributer

Contact Information for Business Card

Vortani

Requirements
Must have
• Names, both office Adresses, email, homepage
Should not have
• Phone Number

```html
<!DOCTYPE html>
<html lang="en">
<head>
<meta charset="utf-8">
<title>Vortani Business Card</title>
<link rel="stylesheet" href="https://fonts.googleapis.com/css2?family=Open+Sans:wght@400;500&family=Poppins:wght@600&display=swap">
<style>
  :root {
    --brand-blue: #3953a4;
    --paper: #ffffff;
    --header-tint: #f5f7f2;
    --ink: #0d0d0d;
    --backdrop: #e9eaeb;
    --on-blue: #ffffff;
  }
  * { box-sizing: border-box; margin: 0; padding: 0; }
  html, body { width: 1200px; height: 1000px; overflow: hidden; }
  body {
    background: var(--backdrop);
    font-family: "Open Sans", Arial, sans-serif;
    position: relative;
  }
  .card {
    position: absolute;
    left: 301px;
    width: 596px;
    height: 341px;
    background: var(--paper);
    overflow: hidden;
  }
  .card--front { top: 120px; }
  .card--back { top: 522px; }

  .front-bands { position: absolute; inset: 0; }

  .wordmark {
    position: absolute;
    left: 0; right: 0;
    text-align: center;
    font-family: "Poppins", Arial, sans-serif;
    font-weight: 600;
    letter-spacing: 0;
    line-height: 1;
    color: var(--ink);
  }
  .card--front .wordmark { top: 142px; font-size: 46px; }
  .card--back .wordmark { top: 38px; font-size: 34px; }

  .back-header {
    position: absolute; left: 0; top: 0; width: 100%; height: 109px;
    background: var(--header-tint);
    border-bottom: 3px solid var(--brand-blue);
  }

  .owners {
    position: absolute; top: 120px; left: 0; width: 100%;
    display: flex; justify-content: center; align-items: center;
    font-family: "Poppins", Arial, sans-serif;
    font-weight: 600; font-size: 21px; color: var(--ink);
  }
  .owners__name { width: 270px; white-space: nowrap; }
  .owners__name--left { text-align: right; padding-right: 10px; }
  .owners__name--right { padding-left: 10px; }
  .owners__divider { width: 2px; height: 30px; background: var(--brand-blue); }
  .role {
    position: absolute; top: 156px; left: 0; width: 100%;
    text-align: center; font-size: 12.5px; color: var(--brand-blue);
  }

  .contact-panel {
    position: absolute; left: 0; top: 179px; width: 100%; height: 162px;
    background: var(--brand-blue); color: var(--on-blue);
    font-size: 11.5px; line-height: 14px;
  }
  .contact-panel__rail { position: absolute; left: 0; top: 0; }
  .contact-row { position: absolute; width: 100%; }
  .contact-row__left { position: absolute; right: 326px; text-align: right; white-space: nowrap; }
  .contact-row__right { position: absolute; left: 326px; white-space: nowrap; }
  .contact-row--email { top: 24px; }
  .contact-row--address { top: 58px; }
  .website {
    position: absolute; top: 128px; left: 0; width: 100%; text-align: center;
  }
</style>
</head>
<body>

<section class="card card--front" aria-label="Card front">
  <svg class="front-bands" width="596" height="341" viewBox="0 0 596 341" aria-hidden="true">
    <polygon points="0,0 596,0 596,61" fill="var(--brand-blue)"/>
    <polygon points="0,280 596,341 0,341" fill="var(--brand-blue)"/>
  </svg>
  <div class="wordmark">Vortani</div>
</section>

<section class="card card--back" aria-label="Card back">
  <header class="back-header">
    <div class="wordmark">Vortani</div>
  </header>

  <div class="owners">
    <span class="owners__name owners__name--left">Lukas Feldhaus</span>
    <span class="owners__divider"></span>
    <span class="owners__name owners__name--right">Imran Qureshi</span>
  </div>
  <p class="role">OWNER</p>

  <div class="contact-panel">
    <svg class="contact-panel__rail" width="596" height="162" viewBox="0 0 596 162" aria-hidden="true">
      <line x1="298" y1="0" x2="298" y2="100" stroke="#fff" stroke-width="1.6"/>
      <g fill="var(--brand-blue)" stroke="#fff" stroke-width="1.6">
        <circle cx="298" cy="32" r="11"/>
        <circle cx="298" cy="71" r="11"/>
        <circle cx="298" cy="110" r="11"/>
      </g>
      <rect x="292" y="28" width="12" height="8" fill="#fff"/>
      <polyline points="292,28 298,33 304,28" fill="none" stroke="var(--brand-blue)" stroke-width="1"/>
      <path d="M298 65 a4 4 0 0 1 4 4 c0 3 -4 7 -4 7 c0 0 -4 -4 -4 -7 a4 4 0 0 1 4 -4z" fill="#fff"/>
      <circle cx="298" cy="69" r="1.5" fill="var(--brand-blue)"/>
      <line x1="294" y1="77" x2="302" y2="77" stroke="#fff" stroke-width="1"/>
      <g fill="none" stroke="#fff" stroke-width="0.9">
        <circle cx="298" cy="110" r="6.5"/>
        <ellipse cx="298" cy="110" rx="3" ry="6.5"/>
        <line x1="291.5" y1="110" x2="304.5" y2="110"/>
        <line x1="292.5" y1="106.5" x2="303.5" y2="106.5"/>
        <line x1="292.5" y1="113.5" x2="303.5" y2="113.5"/>
        <line x1="298" y1="103.5" x2="298" y2="116.5"/>
      </g>
    </svg>

    <div class="contact-row contact-row--email">
      <span class="contact-row__left">lukas@vortani-example.com</span>
      <span class="contact-row__right">imran@vortani-example.com</span>
    </div>
    <div class="contact-row contact-row--address">
      <span class="contact-row__left">Kornblumenweg 14, 08352 Burgstädt<br>Germany</span>
      <span class="contact-row__right">Daska Lane, Sialkot<br>Pakistan</span>
    </div>
    <p class="website">www.vortani-example.com</p>
  </div>
</section>

</body>
</html>
```